VERIDAX Need a luxury modern business card designed.

Need a luxury modern business card designed. refer to the uploaded files for the company name and logo in the zip file under source files. i will making my descion on monday. so please send in before then so if we need to edit we will have the time. we have a trade show coming up and im on a deadline for printer.

Target Market(s)

high end clients

Contact Information for Business Card

Company nAme and logo. Calvin Ostrow Co-Founder / Project Manager Office # 416-555-0193 Cell # 416-555-0147 VERIDAX.CA Calvin@veridax.ca

Font styles to use
Other font styles liked:
• Modern

Requirements
Must have
• Company name and logo, contact info, using the black, gold and white color scheme.

```html
<!DOCTYPE html>
<html lang="en">
<head>
<meta charset="UTF-8">
<title>VERIDAX – Business Card</title>
<link rel="stylesheet" href="https://fonts.googleapis.com/css2?family=Josefin+Sans:wght@300;400&family=Poppins:wght@400;500&display=swap">
<style>
  :root {
    --stage: #1b1b1b;
    --card-dark: #2e2e2e;
    --card-light: #ffffff;
    --card-light-shade: #f0f0f0;
    --ink: #1f1f1f;
    --grey: #6d6d6d;
    --gold: #a8976a;
    --white: #ffffff;
    --rule-dark: #8a8a8a;
    --rule-light: #9a9a9a;
  }
  * { margin: 0; padding: 0; box-sizing: border-box; }
  html, body { width: 1200px; height: 900px; overflow: hidden; }
  body {
    background: var(--stage);
    display: flex;
    flex-direction: column;
    align-items: center;
    justify-content: center;
    gap: 56px;
    font-family: "Poppins", sans-serif;
  }
  .card {
    width: 630px;
    height: 360px;
    position: relative;
    overflow: hidden;
    box-shadow: 0 18px 40px rgba(0,0,0,.55);
  }

  /* ---------- Front ---------- */
  .card--front {
    background: linear-gradient(160deg, var(--card-light) 45%, var(--card-light-shade) 100%);
    color: var(--ink);
  }
  .brand {
    position: absolute;
    text-align: center;
  }
  .brand__name {
    font-family: "Josefin Sans", sans-serif;
    font-weight: 300;
    letter-spacing: .32em;
    line-height: 1;
  }
  .brand__tagline {
    display: flex;
    align-items: center;
    gap: 10px;
    font-family: "Josefin Sans", sans-serif;
    font-weight: 400;
    letter-spacing: .45em;
    text-transform: uppercase;
  }
  .brand__tagline::before,
  .brand__tagline::after {
    content: "";
    flex: 1;
    height: 1px;
  }
  .card--front .brand { left: 60px; top: 44px; width: 300px; }
  .card--front .brand__name { font-size: 40px; color: var(--ink); padding-left: .32em; }
  .card--front .brand__tagline { font-size: 8px; color: var(--grey); margin-top: 10px; }
  .card--front .brand__tagline::before,
  .card--front .brand__tagline::after { background: var(--rule-light); }

  .person { position: absolute; left: 60px; top: 150px; }
  .person__name {
    font-family: "Poppins", sans-serif;
    font-weight: 400;
    font-size: 24px;
    letter-spacing: .06em;
    text-transform: uppercase;
    color: var(--ink);
  }
  .person__name .surname { color: var(--gold); }
  .person__title {
    font-size: 11px;
    letter-spacing: .02em;
    text-transform: uppercase;
    color: var(--grey);
    margin-top: 2px;
  }
  .contact {
    position: absolute;
    left: 60px;
    top: 228px;
    list-style: none;
  }
  .contact li {
    display: flex;
    align-items: center;
    gap: 12px;
    font-size: 14px;
    line-height: 24px;
    color: var(--ink);
  }
  .contact svg { width: 13px; height: 13px; fill: var(--gold); flex: none; }

  .accent-bar {
    position: absolute;
    right: 60px;
    top: 60px;
    width: 2px;
    height: 240px;
    background: linear-gradient(to bottom, var(--ink), rgba(31,31,31,0));
  }

  /* ---------- Back ---------- */
  .card--back {
    background: linear-gradient(150deg, #333 0%, var(--card-dark) 60%, #292929 100%);
  }
  .card--back .brand {
    left: 50%; top: 50%;
    transform: translate(-50%, -50%);
    width: 380px;
  }
  .card--back .brand__name { font-size: 52px; color: var(--white); padding-left: .32em; }
  .card--back .brand__tagline { font-size: 10px; color: #b9b9b9; margin-top: 14px; }
  .card--back .brand__tagline::before,
  .card--back .brand__tagline::after { background: var(--rule-dark); }
</style>
</head>
<body>

<section class="card card--front" aria-label="Business card front">
  <div class="brand">
    <div class="brand__name">VERIDAX</div>
    <div class="brand__tagline">Luxury Landscapes</div>
  </div>

  <div class="person">
    <h1 class="person__name">Calvin <span class="surname">Ostrow</span></h1>
    <p class="person__title">Co-Founder / Project Manager</p>
  </div>

  <ul class="contact">
    <li>
      <svg viewBox="0 0 24 24" aria-hidden="true"><path d="M6.6 10.8a15.1 15.1 0 0 0 6.6 6.6l2.2-2.2c.3-.3.7-.4 1-.2 1.1.4 2.3.6 3.6.6.6 0 1 .4 1 1V20c0 .6-.4 1-1 1A17 17 0 0 1 3 4c0-.6.4-1 1-1h3.5c.6 0 1 .4 1 1 0 1.3.2 2.5.6 3.6.1.3 0 .7-.2 1z"/></svg>
      416 555 0193
    </li>
    <li>
      <svg viewBox="0 0 24 24" aria-hidden="true"><path d="M7 1h10a2 2 0 0 1 2 2v18a2 2 0 0 1-2 2H7a2 2 0 0 1-2-2V3a2 2 0 0 1 2-2zm0 3v13h10V4zm5 15a1.2 1.2 0 1 0 0 2.4 1.2 1.2 0 0 0 0-2.4z"/></svg>
      416 555 0147
    </li>
    <li>
      <svg viewBox="0 0 24 24" aria-hidden="true"><path d="M2 5h20v14H2zm2 2v.5l8 5 8-5V7zm0 2.8V17h16V9.8l-8 5z"/></svg>
      Calvin@veridax.ca
    </li>
    <li>
      <svg viewBox="0 0 24 24" aria-hidden="true"><path d="M12 2a10 10 0 1 0 0 20 10 10 0 0 0 0-20zm6.9 6h-2.9a15 15 0 0 0-1.4-3.6A8 8 0 0 1 18.9 8zM12 4c.8 1.2 1.5 2.5 1.9 4h-3.8c.4-1.5 1.1-2.8 1.9-4zM4.3 14a8 8 0 0 1 0-4h3.3a16 16 0 0 0 0 4zm.8 2h2.9c.3 1.3.8 2.5 1.4 3.6A8 8 0 0 1 5.1 16zM8 8H5.1a8 8 0 0 1 4.3-3.6C8.8 5.5 8.3 6.7 8 8zm4 12c-.8-1.2-1.5-2.5-1.9-4h3.8c-.4 1.5-1.1 2.8-1.9 4zm2.3-6H9.7a14 14 0 0 1 0-4h4.6a14 14 0 0 1 0 4zm.3 5.6c.6-1.1 1.1-2.3 1.4-3.6h2.9a8 8 0 0 1-4.3 3.6zm1.8-5.6a16 16 0 0 0 0-4h3.3a8 8 0 0 1 0 4z"/></svg>
      veridax.ca
    </li>
  </ul>

  <div class="accent-bar" aria-hidden="true"></div>
</section>

<section class="card card--back" aria-label="Business card back">
  <div class="brand">
    <div class="brand__name">VERIDAX</div>
    <div class="brand__tagline">Luxury Landscapes</div>
  </div>
</section>

</body>
</html>
```